Birchwell Landing - Multifamily Development

Birchwell Landing is a Luxury Multifamily Development project located in Orange, NJ. This project will be completed in three phases with the first phase about 75% complete. Each phase will have a different name as follows
CREST Birchwell Landing
RIDGE Birchwell Landing
ZENITHAL Birchwell Landing
We are going to install a banner on the side of the first building which will act as advertising for all buildings. We will eventually need advertising that will be in the windows as well as marketing materials . We want the marketing for this project to be similar for all three phases. At the moment, we are starting with this first simple banner. Attached is a rough idea of the look as well as our color palette. If you feel the color palette is a little too monochrome, feel free to propose an accent color. You can also visit our website to see more info on our company as well as the project. www.tolvarhq.com Finally, if you need AI files (ie. for the logo), we can send to you. Thanks..

```html
<!DOCTYPE html>
<html lang="en">
<head>
<meta charset="UTF-8">
<title>Birchwell Landing – Luxury Apartment Rentals</title>
<link rel="stylesheet" href="https://fonts.googleapis.com/css2?family=Montserrat:wght@300;400;700;800&display=swap">
<style>
  :root {
    --navy: #141a52;
    --wave-light: #02a9e2;
    --wave-deep: #2b3591;
    --white: #ffffff;
    --photo-top: #2f7fae;
    --photo-mid: #3a8fbf;
    --photo-lawn: #2f9a6a;
    --render-sky: #cdd8df;
    --render-warm: #d8ad8a;
    --render-deep: #bb7654;
  }
  * { margin: 0; padding: 0; box-sizing: border-box; }
  html, body { width: 900px; height: 1200px; overflow: hidden; background: var(--navy); }
  .banner {
    position: relative; width: 900px; height: 1200px; overflow: hidden;
    font-family: "Montserrat", sans-serif; color: var(--white); background: var(--navy);
  }
  .hero-photo {
    position: absolute; inset: 0 0 200px 0;
    background:
      linear-gradient(160deg, var(--photo-top) 0%, var(--photo-mid) 45%, transparent 70%),
      linear-gradient(200deg, var(--photo-mid) 40%, var(--photo-lawn) 75%, var(--photo-mid) 100%);
  }
  .shapes { position: absolute; inset: 0; }
  .brand {
    position: absolute; left: 52px; top: 46px;
    display: flex; align-items: center; gap: 12px;
    color: var(--navy); font-weight: 800; font-size: 30px; line-height: 1.05;
  }
  .brand-mark { width: 16px; height: 16px; background: var(--navy); flex: none; }
  .headline { position: absolute; left: 26px; top: 362px; text-transform: uppercase; }
  .headline-project { font-weight: 300; font-size: 48px; letter-spacing: -0.5px; line-height: 1; }
  .headline-offer {
    margin-top: 20px; font-weight: 800; font-size: 67px; line-height: 84px; letter-spacing: 0.5px;
    text-shadow: 0 3px 6px rgba(0,0,0,0.35);
  }
  .feature-ring {
    position: absolute; left: 334px; top: 553px; width: 592px; height: 592px;
    border-radius: 50%; background: var(--white);
  }
  .feature-photo {
    position: absolute; left: 354px; top: 573px; width: 552px; height: 552px; border-radius: 50%;
    background: linear-gradient(165deg, var(--render-sky) 0%, var(--render-warm) 50%, var(--render-deep) 100%);
  }
  .contact { position: absolute; left: 34px; display: flex; align-items: center; gap: 16px; }
  .contact-phone { top: 1009px; }
  .contact-web { top: 1102px; }
  .contact-icon { width: 42px; height: 54px; flex: none; }
  .contact-web .contact-icon { height: 44px; }
  .contact-label { font-weight: 400; font-size: 20px; line-height: 1.3; }
  .contact-value { font-weight: 800; font-size: 26px; line-height: 1.2; }
  .contact-web .contact-value { font-size: 25px; }
</style>
</head>
<body>
<main class="banner">
  <div class="hero-photo" role="img" aria-label="Photo of the brick apartment building with lawn, young trees and a now-leasing flag, tinted blue"></div>

  <svg class="shapes" width="900" height="1200" viewBox="0 0 900 1200" aria-hidden="true">
    <defs>
      <linearGradient id="wave-fill" x1="0.9" y1="0" x2="0.1" y2="1">
        <stop offset="0" stop-color="var(--wave-light)"/>
        <stop offset="1" stop-color="var(--wave-deep)"/>
      </linearGradient>
    </defs>
    <path d="M0 0 H537 C470 80 420 170 360 220 C280 285 150 305 0 298 Z" fill="url(#wave-fill)"/>
    <path d="M0 0 H300 C325 40 320 120 270 150 C210 185 80 175 0 120 Z" fill="var(--white)"/>
    <path d="M0 946 C180 930 360 890 520 790 C650 710 760 670 900 640 V1200 H0 Z" fill="var(--navy)"/>
  </svg>

  <div class="brand">
    <span class="brand-mark"></span>
    <span class="brand-name">Tolvar<br>Properties</span>
  </div>

  <header class="headline">
    <h2 class="headline-project">Birchwell Landing</h2>
    <h1 class="headline-offer">Luxury Apartment<br>Rentals</h1>
  </header>

  <div class="feature-ring"></div>
  <div class="feature-photo" role="img" aria-label="Rendering of the five-storey brick apartment building with street trees"></div>

  <div class="contact contact-phone">
    <svg class="contact-icon" viewBox="0 0 42 54" aria-hidden="true">
      <rect x="1" y="1" width="40" height="52" rx="3" fill="var(--white)"/>
      <rect x="34" y="1" width="3" height="52" fill="var(--navy)"/>
      <path d="M12 16c2-2 4-2 5 0l2 4c1 2 0 3-1 4l-1 1c1 3 4 6 7 8l1-1c1-1 2-2 4-1l4 2c2 1 2 3 0 5-3 3-7 3-12-1-5-4-9-9-10-14-1-3 0-5 1-7z" fill="var(--navy)"/>
    </svg>
    <div>
      <p class="contact-label">More information call us</p>
      <p class="contact-value">555-014-2290</p>
    </div>
  </div>

  <div class="contact contact-web">
    <svg class="contact-icon" viewBox="0 0 44 44" aria-hidden="true">
      <g fill="none" stroke="var(--white)" stroke-width="3">
        <circle cx="22" cy="22" r="19"/>
        <ellipse cx="22" cy="22" rx="8" ry="19"/>
        <line x1="22" y1="3" x2="22" y2="41"/>
        <line x1="3" y1="22" x2="41" y2="22"/>
        <line x1="6" y1="13" x2="38" y2="13"/>
        <line x1="6" y1="31" x2="38" y2="31"/>
      </g>
    </svg>
    <div>
      <p class="contact-label">Visit our website</p>
      <p class="contact-value">https://www.tolvarhq.com/</p>
    </div>
  </div>
</main>
</body>
</html>
```